The hardcover "Crimson Register" (large size, Quarto 4º, 12 × 9 1/2 in, 30.5 × 24.15 cm) in German language as follows:

PURPURNES REGISTER (title)
der herausragendsten Unternehmer und Manager Deutschlands 2013 (subtitle 1)
BERLIN UND BRANDENBURG (subtitle 2, smaller than subtitle 1)

Quorvexa (logo, WMF file attached)

Reason: The solutions are rather too childish and pre-made styles... is there anyone who can make it better? - a professional-looking business book (encyclopedia style, should have no color-pictures, no author's name, logo smaller due to the large size book)

Target Market(s)

business community

Requirements
Must have
• encyclopedia style large size book
must look professional and expensive

Nice to have
• - gold-color hardcover, or some gold-color elements
- some simple and decent graphic element (e.g. an ancient column, or some other architectural detail), if any
Should not have
• no color-pictures
no author's name

```html
<!DOCTYPE html>
<html lang="de">
<head>
<meta charset="utf-8">
<title>Purpurnes Register – Buchcover</title>
<link rel="stylesheet" href="https://fonts.googleapis.com/css2?family=Cinzel:wght@500&family=Montserrat:wght@700&display=swap">
<style>
  :root {
    --page-bg: #ffffff;
    --leather-light: #e6c98a;
    --leather-mid: #9a7034;
    --leather-dark: #4a2f14;
    --leather-edge: #2e1c0b;
    --title-top: #ff6a1a;
    --title-bottom: #ffd21a;
    --rule-yellow: #f2d21c;
    --subtitle-white: #fff8ea;
    --brand-gold: #f2d21c;
  }
  * { margin: 0; padding: 0; box-sizing: border-box; }
  html, body {
    width: 1000px;
    height: 1200px;
    overflow: hidden;
    background: var(--page-bg);
  }
  .canvas {
    position: relative;
    width: 1000px;
    height: 1200px;
  }
  .cover {
    position: absolute;
    left: 160px;
    top: 110px;
    width: 680px;
    height: 980px;
    overflow: hidden;
    box-shadow: 0 10px 30px rgba(0,0,0,0.35);
  }
  .cover__leather {
    position: absolute;
    inset: 0;
    background:
      radial-gradient(ellipse 60% 45% at 48% 58%, var(--leather-light) 0%, var(--leather-mid) 45%, var(--leather-dark) 85%, var(--leather-edge) 100%);
  }
  .cover__title {
    position: absolute;
    top: 150px;
    left: 0;
    right: 0;
    text-align: center;
    font-family: "Montserrat", "Century Gothic", sans-serif;
    font-weight: 700;
    line-height: 1.02;
    letter-spacing: 1px;
  }
  .cover__title-line {
    display: block;
    background: linear-gradient(180deg, var(--title-top) 0%, var(--title-bottom) 100%);
    -webkit-background-clip: text;
    background-clip: text;
    color: transparent;
    filter: drop-shadow(0 4px 5px rgba(0,0,0,0.55));
  }
  .cover__title-line--first { font-size: 86px; }
  .cover__title-line--second { font-size: 94px; }
  .cover__subtitle {
    position: absolute;
    left: 50px;
    right: 40px;
    top: 770px;
    text-align: center;
    font-family: "Cinzel", Georgia, serif;
    font-weight: 500;
    color: var(--subtitle-white);
    text-shadow: 0 1px 3px rgba(0,0,0,0.6);
  }
  .cover__rule {
    height: 3px;
    background: var(--rule-yellow);
    margin: 0 auto;
  }
  .cover__rule--top { width: 340px; margin-bottom: 8px; }
  .cover__rule--bottom { width: 340px; margin-top: 6px; margin-bottom: 10px; }
  .cover__subtitle-main {
    font-size: 25px;
    line-height: 1.05;
  }
  .cover__subtitle-region {
    font-size: 17px;
    letter-spacing: 0.5px;
  }
  .cover__brand {
    position: absolute;
    left: 0;
    right: 0;
    bottom: 48px;
    display: flex;
    justify-content: center;
    align-items: center;
    gap: 8px;
    font-family: "Cinzel", Georgia, serif;
    font-weight: 500;
    font-size: 16px;
    letter-spacing: 2px;
    color: var(--brand-gold);
  }
  .cover__brand-mark {
    width: 10px;
    height: 10px;
    border-radius: 50%;
    background: var(--brand-gold);
  }
</style>
</head>
<body>
  <div class="canvas">
    <section class="cover">
      <div class="cover__leather" role="img" aria-label="Braun-goldene Ledertextur des Einbands"></div>
      <h1 class="cover__title">
        <span class="cover__title-line cover__title-line--first">PURPURNES</span>
        <span class="cover__title-line cover__title-line--second">REGISTER</span>
      </h1>
      <div class="cover__subtitle">
        <div class="cover__rule cover__rule--top"></div>
        <p class="cover__subtitle-main">Der Herausragendsten Unternehmer und<br>Manager Deutschlands 2013</p>
        <div class="cover__rule cover__rule--bottom"></div>
        <p class="cover__subtitle-region">Berlin und Brandenburg</p>
      </div>
      <div class="cover__brand">
        <span class="cover__brand-mark"></span>
        <span class="cover__brand-name">Quorvexa</span>
      </div>
    </section>
  </div>
</body>
</html>
```